Geschäftspapiere für medizinische Schutzausrüstung
Zielgruppe
Medizinische Schutzausrüstung für Deutschland.
Zertifiziert, schnell und unkompliziert.
Für Einrichtungen im Bereich Medizin & Pflege, systemrelevante Industrien sowie für öffentliche Träger.
Aufgabenstellung
Es sollte clean sein, Farben wie , Weiß, blau, grün, wären von Vorteil. Habe keine besondere Vorstellungen lasse mich gerne überraschen.
Siehe .. www.kvoltaq.de

```html
<!DOCTYPE html>
<html lang="de">
<head>
<meta charset="utf-8">
<title>Briefbogen – Nordwell Care Supply</title>
<link href="https://fonts.googleapis.com/css2?family=Lato:wght@400;700;900&display=swap" rel="stylesheet">
<style>
  :root {
    --navy: #1d2a44;
    --grey-text: #5b6170;
    --sage: #8aae8e;
    --straw: #d8cf78;
    --gold: #c8b65a;
    --rule-blue: #8aa7c4;
    --paper: #ffffff;
  }
  html, body {
    margin: 0;
    padding: 0;
    width: 904px;
    height: 1200px;
    overflow: hidden;
    background: var(--paper);
    font-family: "Lato", Arial, sans-serif;
    color: var(--navy);
  }
  .letterhead {
    position: relative;
    width: 904px;
    height: 1200px;
    background: var(--paper);
  }
  .brand {
    position: absolute;
    top: 128px;
    left: 0;
    width: 904px;
    text-align: center;
  }
  .brand-name {
    display: inline-flex;
    align-items: center;
    gap: 10px;
    font-weight: 900;
    font-size: 20px;
    letter-spacing: 0.5px;
    text-transform: uppercase;
    color: var(--navy);
  }
  .brand-dot {
    width: 12px;
    height: 12px;
    border-radius: 50%;
    background: var(--sage);
  }
  .brand-tagline {
    margin-top: 6px;
    font-size: 8.5px;
    font-weight: 700;
    letter-spacing: 3.6px;
    text-transform: uppercase;
    color: var(--navy);
  }
  .return-address {
    position: absolute;
    top: 214px;
    left: 95px;
    font-size: 9.5px;
    color: var(--grey-text);
    border-bottom: 1px solid #9aa0aa;
    padding-bottom: 1px;
  }
  .return-address .sep { color: #3a6db0; }
  .fold-mark {
    position: absolute;
    left: 0;
    width: 33px;
    height: 1px;
    background: var(--rule-blue);
  }
  .fold-mark.upper { top: 422px; }
  .fold-mark.lower { top: 823px; }
  .footer {
    position: absolute;
    left: 0;
    top: 1135px;
    width: 904px;
    font-size: 11px;
    color: var(--navy);
  }
  .footer .col {
    position: absolute;
    top: 0;
    line-height: 18px;
    white-space: nowrap;
  }
  .footer .contact-line {
    display: flex;
    align-items: center;
    gap: 6px;
  }
  .footer .icon { width: 12px; height: 12px; flex: none; }
  .col.address { left: 48px; top: 2px; line-height: 16px; }
  .col.phone { left: 176px; }
  .col.web { left: 293px; }
  .footer .divider {
    position: absolute;
    left: 474px;
    top: 3px;
    width: 1px;
    height: 30px;
    background: var(--gold);
  }
  .col.bank, .col.register {
    font-size: 9.5px;
    font-weight: 700;
    line-height: 18px;
  }
  .col.bank { left: 517px; }
  .col.register { left: 724px; }
  .label { display: inline-block; }
  .col.bank .label { width: 30px; }
  .col.register .label { width: 58px; }
  .value { font-weight: 700; }
  .base-band {
    position: absolute;
    left: 0;
    top: 1174px;
    width: 904px;
    height: 15px;
  }
</style>
</head>
<body>
<main class="letterhead">
  <header class="brand">
    <div class="brand-name"><span class="brand-dot"></span>Nordwell Care Supply</div>
    <div class="brand-tagline">Zertifiziert &amp; Schnell</div>
  </header>

  <div class="return-address">Lindenweg 12 <span class="sep">•</span> 30159 Musterstadt</div>

  <div class="fold-mark upper"></div>
  <div class="fold-mark lower"></div>

  <footer class="footer">
    <div class="col address">Ahornstraße 8<br>31135 Feldheim</div>

    <div class="col phone">
      <div class="contact-line">
        <svg class="icon" viewBox="0 0 12 12" aria-hidden="true"><path d="M2.5 1.5 L4.5 1.5 L5.3 3.8 L4 4.8 Q5 7 7.2 8 L8.2 6.7 L10.5 7.5 L10.5 9.5 Q5 10 2.5 1.5Z" fill="none" stroke="var(--gold)" stroke-width="1"/></svg>
        <span>00000 48213</span>
      </div>
      <div class="contact-line">
        <svg class="icon" viewBox="0 0 12 12" aria-hidden="true"><rect x="3" y="1.5" width="6" height="3" fill="none" stroke="var(--gold)"/><rect x="1.5" y="4.5" width="9" height="4" rx="1" fill="none" stroke="var(--gold)"/><rect x="3" y="7" width="6" height="3.5" fill="none" stroke="var(--gold)"/></svg>
        <span>00000 27654</span>
      </div>
    </div>

    <div class="col web">
      <div class="contact-line">
        <svg class="icon" viewBox="0 0 12 12" aria-hidden="true"><circle cx="6" cy="6" r="4.6" fill="none" stroke="var(--gold)"/><ellipse cx="6" cy="6" rx="2" ry="4.6" fill="none" stroke="var(--gold)"/><line x1="1.4" y1="6" x2="10.6" y2="6" stroke="var(--gold)"/></svg>
        <span>www.nordwellcare.de</span>
      </div>
      <div class="contact-line">
        <svg class="icon" viewBox="0 0 12 12" aria-hidden="true"><rect x="1.5" y="3" width="9" height="6.5" fill="none" stroke="var(--gold)"/><polyline points="1.5,3 6,7 10.5,3" fill="none" stroke="var(--gold)"/></svg>
        <span>info@nordwellcare.de</span>
      </div>
    </div>

    <div class="divider"></div>

    <div class="col bank">
      <div><span class="label">BIC</span><span class="value">XQRTDEF1ABC</span></div>
      <div><span class="label">IBAN</span><span class="value">DE00 1234 5678 9012 3456 78</span></div>
    </div>

    <div class="col register">
      <div><span class="label">USt-IdNr.:</span><span class="value">DE000111222</span></div>
      <div><span class="label">Register-Nr.</span><span class="value">HRA 9912</span></div>
    </div>
  </footer>

  <svg class="base-band" viewBox="0 0 904 15" aria-hidden="true">
    <rect x="0" y="0" width="904" height="15" fill="var(--sage)"/>
    <polygon points="766,15 778,0 798,0 786,15" fill="var(--straw)"/>
    <polygon points="792,15 804,0 824,0 812,15" fill="var(--straw)"/>
    <polygon points="818,15 830,0 850,0 838,15" fill="var(--straw)"/>
    <polygon points="844,15 856,0 876,0 864,15" fill="#ffffff"/>
  </svg>
</main>
</body>
</html>
```